Home page and features page design for SaaS company

We're looking for designs for a home page and a features page of a new website (possibly more pages to be commissioned thereafter). The website is called 'Brightly Afloat' and is a service that helps swimming clubs and schools reduce administration.

The website will have a clean, minimalist, modern feel but not corporate. Here's an idea of the type of style: https://squadlio.net/pages/payments

At the top of the home page (above the fold) will show the two personas that the website is targeting (Swimming clubs and Swimming Schools) on a styled background (no cheesy stock images please!). Those personas can be represented as an illustration (see page 2 for an example), line art graphic or icon and will link through to a features page.

For your information, the type of people that are members of swimming clubs include beginners, competitive squads and adult swimmers. People that attend a swimming school are typically children learning to swim. If you can represent the above in simple line art illustrations/graphics/icons that match the style of our logo - great!

Below the fold on the home page will be an illustration of the main functions of the site (with our logo central to that) and at the bottom of the page will be what they get for free, testimonials and a call to action for booking a demo.

I've attached a simple wireframe of the home page for your information.

The second page is the features page. This summarises the benefits of each major feature. Each feature listed on the page is separated by a call to action. Here's a link to the content of the features page: http://webhost4.qarvik-advisory.com/KLTsalespages/swimming/swim-club-management-software.html

Don't take a lead from the look / feel / design of this page. I don't like it (hence I'm on here to find a better design!). One thing I'd like to incorporate is a snippet preview of a screenshot on the features page (a bit like in the example). The user can click on this and the full screenshot will load in a pop-up.

The style of the features page should flow from the home page.
Updates

Project Deadline Extended
Reason: Extending deadline to allow more quality designs and give those that have submitted time to make any revisions.

Target Market(s)

Swimming clubs and swimming schools

Industry/Entity Type

Internet

Number of Pages Required

2 page

Font styles to use
Sans Serif

Colors
33a6d7
33b8a4

Requirements
Must have
• Clean, minimalist, modern feel but not corporate. Here's an idea of the type of style: https://squadlio.net/pages/payments
Should not have
• Unstylised stock photographs

```html
<!DOCTYPE html>
<html lang="en">
<head>
<meta charset="utf-8">
<title>Brightly Afloat – Membership software for swimming clubs and schools</title>
<link href="https://fonts.googleapis.com/css2?family=Lato:ital,wght@0,300;0,400;0,700;1,400&family=Roboto+Slab:wght@700&display=swap" rel="stylesheet">
<style>
:root{
  --teal:#33b8a4;
  --blue:#33a6d7;
  --accent-blue:#1c8fd3;
  --ink:#333a3f;
  --muted:#6b7175;
  --grey-band:#ebebeb;
  --footer:#363636;
  --footer-line:#8a8a8a;
  --field:#f6eeee;
  --white:#ffffff;
}
*{box-sizing:border-box;margin:0;padding:0}
html,body{width:1200px;height:2970px;overflow:hidden}
body{font-family:'Lato',sans-serif;color:var(--ink);background:var(--white);position:relative}
a{color:inherit;text-decoration:none}

/* Hero */
.hero{position:absolute;left:0;top:0;width:1200px;height:565px;
  background:linear-gradient(160deg,var(--teal) 0%,#35b3b3 55%,var(--blue) 100%)}
.brand{position:absolute;left:88px;top:46px;display:flex;align-items:center;gap:10px;
  font-size:22px;font-weight:700;color:var(--white)}
.brand-dot{width:26px;height:26px;border-radius:50%;background:var(--white)}
.main-nav{position:absolute;right:84px;top:48px;display:flex;align-items:center;gap:26px;
  font-size:11px;font-weight:700;color:var(--white);text-transform:uppercase}
.signin{background:var(--accent-blue);padding:8px 18px;border-radius:2px}
.hero-title{position:absolute;left:0;width:1200px;top:158px;text-align:center;
  color:var(--white);font-weight:300;font-size:37px;line-height:52px}
.persona{position:absolute;top:288px;width:240px;text-align:center;color:var(--white)}
.persona-club{left:292px}
.persona-school{left:658px}
.persona-art{width:160px;height:160px;margin:0 auto;border-radius:50%;border:6px solid #e9ecee;
  background:radial-gradient(circle,#ffffff 55%,#eef1f3 100%);box-shadow:0 4px 10px rgba(0,0,0,.18)}
.persona-name{font-size:22px;margin-top:18px}
.persona-link{display:inline-block;font-size:13px;margin-top:14px;text-decoration:underline}

/* Benefits */
.section-title{position:absolute;left:0;width:1200px;text-align:center;font-weight:400;font-size:38px;color:var(--ink)}
.benefits-title{top:630px}
.benefits-map{position:absolute;left:0;top:700px}
.benefit-label{font-family:'Lato',sans-serif;font-size:13px;fill:var(--ink)}

/* How it works */
.how{position:absolute;left:0;top:1297px;width:1200px;height:495px;background:var(--grey-band)}
.how-title{top:1353px}
.step{position:absolute;top:1478px;width:220px;text-align:center}
.step-icon{width:96px;height:96px;margin:0 auto;border-radius:50%;background:var(--white);
  border:4px solid #e1e1e1;display:flex;align-items:center;justify-content:center}
.step-active .step-icon{background:var(--teal);border-color:#bfe6df;box-shadow:0 0 0 3px var(--teal)}
.step-name{font-size:14px;font-weight:700;margin-top:22px}
.step-active .step-name{color:var(--blue);font-weight:400}
.step-text{font-size:11.5px;line-height:20px;color:var(--muted);margin-top:10px}
.step-arrow{position:absolute;top:1520px}

/* Testimonials */
.testimonials-title{top:1862px}
.testimonial-photo{position:absolute;left:93px;top:1948px;width:224px;height:206px;border:2px solid var(--teal);
  background:linear-gradient(135deg,#8fd0de 0%,#e7b79a 55%,#4eb3cc 100%)}
.testimonial-rule{position:absolute;left:386px;top:1950px;width:1px;height:200px;background:#dcdcdc}
.quote-mark{position:absolute;left:410px;top:1938px;font-family:'Roboto Slab',serif;font-size:44px;color:var(--teal)}
.quote-text{position:absolute;left:445px;top:1976px;width:660px;font-style:italic;font-size:13.5px;line-height:24px;color:#555}
.quote-author{position:absolute;left:445px;top:2060px;font-family:'Roboto Slab',serif;font-size:16px;color:var(--blue)}
.quote-author span{font-family:'Lato',sans-serif;font-size:11px;color:#888;font-weight:400}
.slider-btn{position:absolute;top:2104px;width:36px;height:36px;display:flex;align-items:center;justify-content:center}
.slider-prev{left:438px;background:var(--teal)}
.slider-next{left:484px;background:#555}

/* Call to action */
.cta{position:absolute;left:0;top:2238px;width:1200px;height:370px;
  background:linear-gradient(90deg,#6f6a63 0%,#7d786e 45%,#5f8b93 75%,#7aa9ae 100%)}
.cta-title{position:absolute;left:84px;top:2320px;font-size:37px;font-weight:400;color:var(--white)}
.cta-text{position:absolute;left:85px;top:2382px;width:700px;font-size:11.5px;line-height:20px;color:#f1f1f1}
.cta-button{position:absolute;left:85px;top:2465px;width:198px;height:57px;background:var(--accent-blue);
  color:var(--white);font-size:20px;font-weight:700;display:flex;align-items:center;justify-content:center}

/* Footer */
.footer{position:absolute;left:0;top:2608px;width:1200px;height:362px;background:var(--footer);color:#e6e6e6}
.footer-col{position:absolute;top:38px}
.footer-heading{font-size:14px;text-transform:uppercase;padding-bottom:8px;border-bottom:1px solid var(--footer-line);width:220px}
.contact-list{list-style:none;margin-top:26px;font-size:11px;line-height:22px}
.contact-list li{display:flex;align-items:center;gap:16px}
.social{display:flex;gap:8px;margin-top:18px}
.social span{width:12px;height:12px;border-radius:50%;background:#e6e6e6}
.quick-links{list-style:none;margin-top:16px;font-size:11px;line-height:26.5px}
.quick-links li::before{content:"\25B8";margin-right:14px}
.message-form{margin-top:12px;width:320px;display:grid;grid-template-columns:1fr 1fr;gap:10px 8px}
.field{background:var(--field);height:32px;font-size:9.5px;color:#777;padding:10px 12px}
.field-wide{grid-column:1 / 3}
.field-tall{height:90px}
.send-btn{width:122px;height:34px;background:var(--accent-blue);color:var(--white);font-size:12px;
  display:flex;align-items:center;justify-content:center;margin-top:12px}
.copyright{position:absolute;left:88px;top:316px;font-size:10.5px;color:#e6e6e6}
</style>
</head>
<body>

<header class="hero">
  <a class="brand" href="#"><span class="brand-dot"></span>Brightly Afloat</a>
  <nav class="main-nav">
    <a href="#">About us</a><a href="#">Pricing</a><a href="#">Free resources</a>
    <a href="#">Free account</a><a href="#">Contact us</a><a class="signin" href="#">Sign-in</a>
  </nav>
  <h1 class="hero-title">Membership software<br>for swimming clubs and schools</h1>
  <div class="persona persona-club">
    <div class="persona-art" role="img" aria-label="Illustration of a swimming club coach holding a clipboard"></div>
    <div class="persona-name">Swimming Clubs</div>
    <a class="persona-link" href="#">Find out More &nbsp;›</a>
  </div>
  <div class="persona persona-school">
    <div class="persona-art" role="img" aria-label="Illustration of a swimmer with cap and towel"></div>
    <div class="persona-name">Swimming Schools</div>
    <a class="persona-link" href="#">Find out More &nbsp;›</a>
  </div>
</header>

<h2 class="section-title benefits-title">Our benefits</h2>
<svg class="benefits-map" width="1200" height="560" viewBox="0 700 1200 560" aria-label="Benefits diagram">
  <defs>
    <radialGradient id="hubFill" cx="50%" cy="45%" r="55%">
      <stop offset="0%" stop-color="#7fd3c8"/><stop offset="100%" stop-color="#3cb5aa"/>
    </radialGradient>
  </defs>
  <g stroke="#33a6b6" stroke-width="1.5">
    <line x1="610" y1="986" x2="610" y2="802"/>
    <line x1="610" y1="986" x2="762" y2="842"/>
    <line x1="610" y1="986" x2="816" y2="986"/>
    <line x1="610" y1="986" x2="772" y2="1118"/>
    <line x1="610" y1="986" x2="610" y2="1162"/>
    <line x1="610" y1="986" x2="454" y2="1118"/>
    <line x1="610" y1="986" x2="400" y2="986"/>
    <line x1="610" y1="986" x2="460" y2="842"/>
  </g>
  <circle cx="610" cy="986" r="118" fill="#e3f3f1"/>
  <circle cx="610" cy="986" r="112" fill="url(#hubFill)"/>
  <text x="610" y="993" text-anchor="middle" font-family="Lato,sans-serif" font-weight="700" font-size="22" fill="#ffffff">Brightly Afloat</text>
  <g fill="#ffffff" stroke="#33a6b6" stroke-width="1.8">
    <circle cx="610" cy="802" r="21"/><circle cx="762" cy="842" r="21"/><circle cx="816" cy="986" r="21"/>
    <circle cx="772" cy="1118" r="21"/><circle cx="610" cy="1162" r="21"/><circle cx="454" cy="1118" r="21"/>
    <circle cx="400" cy="986" r="21"/><circle cx="460" cy="842" r="21"/>
  </g>
  <g fill="none" stroke="#33a6b6" stroke-width="1.6">
    <rect x="604" y="792" width="12" height="20" rx="2"/>
    <path d="M755 834h10l4 4v13h-14z"/>
    <rect x="807" y="980" width="18" height="12"/><line x1="812" y1="983" x2="812" y2="989"/>
    <rect x="763" y="1112" width="18" height="13"/><path d="M763 1112l9 7 9-7"/>
    <path d="M598 1160q6-5 12 0t12 0M598 1166q6-5 12 0t12 0"/>
    <circle cx="448" cy="1114" r="4"/><circle cx="460" cy="1114" r="4"/><path d="M442 1126q6-8 12 0q6-8 12 0"/>
    <rect x="391" y="977" width="18" height="18"/><line x1="395" y1="983" x2="405" y2="983"/><line x1="395" y1="989" x2="405" y2="989"/>
    <rect x="452" y="832" width="16" height="20"/><circle cx="460" cy="839" r="3"/>
  </g>
  <text class="benefit-label" x="610" y="763" text-anchor="middle">Online payments</text>
  <text class="benefit-label" x="748" y="805">Financial reporting</text>
  <text class="benefit-label" x="848" y="990">Membership data</text>
  <text class="benefit-label" x="746" y="1165">Group email</text>
  <text class="benefit-label" x="610" y="1210" text-anchor="middle">Galas</text>
  <text class="benefit-label" x="502" y="1165" text-anchor="end">Event management</text>
  <text class="benefit-label" x="368" y="990" text-anchor="end">Attendance register</text>
  <text class="benefit-label" x="474" y="811" text-anchor="end">Online registrations</text>
</svg>

<section class="how" aria-label="How it works"></section>
<h2 class="section-title how-title">How it works</h2>

<div class="step" style="left:82px">
  <div class="step-icon"><svg width="36" height="36" viewBox="0 0 36 36" fill="none" stroke="#777" stroke-width="2"><path d="M14 6h16v24H14M4 18h18M16 12l6 6-6 6"/></svg></div>
  <div class="step-name">Access to Exclusive Tools</div>
  <div class="step-text">We have over 100 great features and functions to help cut down admin and increase payment collection.</div>
</div>
<div class="step" style="left:345px">
  <div class="step-icon"><svg width="38" height="36" viewBox="0 0 38 36" fill="none" stroke="#777" stroke-width="2"><path d="M10 26a8 8 0 0 1 1-16 10 10 0 0 1 19 3 6 6 0 0 1-1 13"/><path d="M15 20a5 5 0 0 1 9-2M24 24a5 5 0 0 1-9 2"/></svg></div>
  <div class="step-name">Software updates</div>
  <div class="step-text">We continuously listen to our clients and develop functionality in line with their feedback to help you improve efficiencies and save time.</div>
</div>
<div class="step step-active" style="left:615px">
  <div class="step-icon"><svg width="38" height="34" viewBox="0 0 38 34" fill="none" stroke="#ffffff" stroke-width="2"><rect x="4" y="4" width="30" height="20"/><path d="M14 30h10M19 24v6M9 10h10M9 15h14"/></svg></div>
  <div class="step-name">Account Setup</div>
  <div class="step-text">We take time to understand how your club works and set your account to maximise efficiencies.</div>
</div>
<div class="step" style="left:884px">
  <div class="step-icon"><svg width="36" height="38" viewBox="0 0 36 38" fill="#777"><circle cx="18" cy="14" r="9"/><path d="M4 36c2-10 8-12 14-12s12 2 14 12z"/></svg></div>
  <div class="step-name">First class support</div>
  <div class="step-text">From your first training session to on going support, we're here to help you get the best from the system. You can reach us by chat, email or video call 6 days a week.</div>
</div>
<svg class="step-arrow" style="left:298px" width="50" height="16" viewBox="0 0 50 16"><path d="M0 8h46M38 2l8 6-8 6" stroke="#666" stroke-width="2" fill="none"/></svg>
<svg class="step-arrow" style="left:570px" width="50" height="16" viewBox="0 0 50 16"><path d="M0 8h46M38 2l8 6-8 6" stroke="#666" stroke-width="2" fill="none"/></svg>
<svg class="step-arrow" style="left:838px" width="50" height="16" viewBox="0 0 50 16"><path d="M0 8h46M38 2l8 6-8 6" stroke="#666" stroke-width="2" fill="none"/></svg>

<h2 class="section-title testimonials-title">Testimonials</h2>
<div class="testimonial-photo" role="img" aria-label="Photo of a smiling young swimmer with goggles at the pool edge"></div>
<div class="testimonial-rule"></div>
<div class="quote-mark">&ldquo;</div>
<p class="quote-text">Lorem Ipsum is simply dummy text of the printing and typesetting industry. Lorem Ipsum has been the industry's standard dummy text ever since the 1500s, when an unknown printer took a galley of type and scrambled it to make a type specimen book. It has survived not only five centuries, but also the leap into .!!</p>
<div class="quote-author">Edith R Caldwell, <span>Harbor Works Ohio.</span></div>
<a class="slider-btn slider-prev" href="#" aria-label="Previous"><svg width="12" height="16" viewBox="0 0 12 16"><path d="M9 2L3 8l6 6" stroke="#fff" stroke-width="2" fill="none"/></svg></a>
<a class="slider-btn slider-next" href="#" aria-label="Next"><svg width="12" height="16" viewBox="0 0 12 16"><path d="M3 2l6 6-6 6" stroke="#fff" stroke-width="2" fill="none"/></svg></a>

<section class="cta" role="img" aria-label="Photo of children in sunglasses smiling by the pool"></section>
<h2 class="cta-title">Book a free demo now</h2>
<p class="cta-text">Lorem Ipsum is simply dummy text of the printing and typesetting industry. Lorem Ipsum has been the industry's standard dummy text ever since the 1500s, when an unknown printer took a galley of type and scrambled it</p>
<a class="cta-button" href="#">Book Now</a>

<footer class="footer">
  <div class="footer-col" style="left:85px">
    <div class="footer-heading">Contact details</div>
    <ul class="contact-list">
      <li><svg width="8" height="11" viewBox="0 0 8 11"><path d="M4 0a4 4 0 0 1 4 4c0 3-4 7-4 7S0 7 0 4a4 4 0 0 1 4-4z" fill="#e6e6e6"/></svg>2210 Fenwick Road, LARKDALE, Oregon, 97301</li>
      <li><svg width="9" height="9" viewBox="0 0 9 9"><path d="M1 0h2l1 2-1 1q1 2 3 3l1-1 2 1v2l-1 1C4 9 0 5 0 1z" fill="#e6e6e6"/></svg>+0198 765 432</li>
      <li><svg width="10" height="8" viewBox="0 0 10 8"><rect width="10" height="8" fill="#e6e6e6"/></svg>hello@brightlyafloat.net</li>
    </ul>
    <div class="social"><span></span><span></span><span></span><span></span></div>
  </div>
  <div class="footer-col" style="left:442px">
    <div class="footer-heading">Quick link</div>
    <ul class="quick-links">
      <li>Home</li><li>About us</li><li>Pricing</li><li>Free resources</li><li>Free account</li><li>Contact us</li>
    </ul>
  </div>
  <div class="footer-col" style="left:797px">
    <div class="footer-heading" style="width:318px">Leave message</div>
    <div class="message-form">
      <div class="field field-wide">Name</div>
      <div class="field">Email</div>
      <div class="field">Phone</div>
      <div class="field field-wide field-tall">Subject</div>
    </div>
    <a class="send-btn" href="#">SEND NOW</a>
  </div>
  <div class="copyright">Copyright © 2017 Brightly Afloat. All Rights Reserved.</div>
</footer>

</body>
</html>
```